Innovative tech company looking for a new look for business card

We need a business card revamp- our current design is amazingly dated and in need of a new vision. The Delta is logo that is used, but other than that and the company name - we are open to everything- red is the color of choice typically due to delta. VN is a National credit reporting agency servicing lending institutions for more than 24 years.

***We want a minimal, clean design, we want to move away from the harsh- red, black and white feel. The files uploaded are to show what we are currently using and exactly what we want to move AWAY from.

Thanks you to all!

We are looking for a "lighter" feel more "oriel-esque." We want to move away from the harsh black , white, and red. The files I uploaded were more to show what we currently have and really want to move away from. I am going to edit the brief to be sure this is expressed.

Reason: Still looking for options....

Reason: Still looking for more designs -

```html
<!DOCTYPE html>
<html lang="en">
<head>
<meta charset="utf-8">
<title>Verity Networks – Business Card</title>
<link rel="stylesheet" href="https://fonts.googleapis.com/css2?family=Montserrat:wght@400;500;600;700&display=swap">
<style>
  :root {
    --backdrop: #efedec;
    --card: #ffffff;
    --ink: #3a3435;
    --muted: #7a7273;
    --accent: #e0675c;
    --accent-soft: #f3b8b0;
    --band-start: #fbeeec;
    --band-end: #f4e4e1;
  }
  * { box-sizing: border-box; margin: 0; padding: 0; }
  html, body { width: 1200px; height: 735px; overflow: hidden; }
  body {
    background: var(--backdrop);
    font-family: "Montserrat", Arial, sans-serif;
    color: var(--ink);
    position: relative;
  }
  .card {
    position: absolute;
    width: 520px;
    height: 300px;
    background: var(--card);
    box-shadow: 0 6px 18px rgba(80, 60, 60, 0.08);
    overflow: hidden;
  }
  .card--back { left: 50px; top: 218px; }
  .card--front { left: 630px; top: 218px; }

  .brand {
    display: flex;
    align-items: center;
    gap: 10px;
  }
  .brand__dot {
    width: 14px; height: 14px;
    background: var(--accent);
  }
  .brand__name {
    font-weight: 600;
    color: var(--ink);
    text-transform: uppercase;
    letter-spacing: 0.06em;
    line-height: 1.05;
  }

  .card--back .brand {
    position: absolute;
    inset: 0;
    justify-content: center;
  }
  .card--back .brand__dot { width: 22px; height: 22px; }
  .card--back .brand__name { font-size: 32px; }

  .card--front .brand {
    position: absolute;
    left: 150px; top: 26px;
  }
  .card--front .brand__name { font-size: 20px; }
  .tagline {
    position: absolute;
    left: 174px; top: 78px;
    font-size: 8px;
    color: var(--accent);
    letter-spacing: 0.02em;
  }

  .swoosh { position: absolute; left: 0; top: 0; }

  .person {
    position: absolute;
    left: 26px; top: 100px;
  }
  .person__name {
    font-size: 15px;
    font-weight: 600;
    color: var(--accent);
    letter-spacing: 0.05em;
    text-transform: uppercase;
  }
  .person__title {
    font-size: 10px;
    color: var(--muted);
    margin-top: 3px;
  }

  .address {
    position: absolute;
    right: 26px; top: 100px;
    text-align: right;
    font-size: 10px;
    font-style: normal;
    font-weight: 500;
    color: var(--muted);
    line-height: 1.45;
  }

  .contacts {
    position: absolute;
    right: 26px; top: 156px;
    list-style: none;
    font-size: 9px;
    color: var(--muted);
  }
  .contacts li {
    display: flex;
    justify-content: flex-end;
    align-items: center;
    gap: 7px;
    height: 15px;
  }
  .contacts svg { width: 9px; height: 9px; fill: var(--accent); }
</style>
</head>
<body>

  <section class="card card--back" aria-label="Card back">
    <div class="brand">
      <span class="brand__dot"></span>
      <span class="brand__name">Verity Networks</span>
    </div>
  </section>

  <section class="card card--front" aria-label="Card front">
    <svg class="swoosh" width="520" height="300" viewBox="0 0 520 300" aria-hidden="true">
      <defs>
        <linearGradient id="band-fill" x1="0" y1="0" x2="1" y2="0">
          <stop offset="0" stop-color="var(--band-start)"/>
          <stop offset="1" stop-color="var(--band-end)"/>
        </linearGradient>
      </defs>
      <path d="M0,156 C150,164 250,234 520,256 L520,280 C260,262 140,218 0,212 Z" fill="url(#band-fill)"/>
      <path d="M0,148 C150,156 250,226 520,248" fill="none" stroke="var(--accent)" stroke-width="1.5"/>
      <path d="M0,220 C140,226 260,272 520,290" fill="none" stroke="var(--accent-soft)" stroke-width="1.5"/>
    </svg>

    <div class="brand">
      <span class="brand__dot"></span>
      <span class="brand__name">Verity<br>Networks</span>
    </div>
    <p class="tagline">Advanced Credit Reporting Services</p>

    <div class="person">
      <p class="person__name">Marcus Delane</p>
      <p class="person__title">Managing Director</p>
    </div>

    <address class="address">
      27 Harbor Point<br>Linden Road
    </address>

    <ul class="contacts">
      <li>555 014 2268
        <svg viewBox="0 0 24 24"><path d="M6.6 10.8a15 15 0 0 0 6.6 6.6l2.2-2.2a1 1 0 0 1 1-.25 11.4 11.4 0 0 0 3.6.57 1 1 0 0 1 1 1V20a1 1 0 0 1-1 1A17 17 0 0 1 3 4a1 1 0 0 1 1-1h3.5a1 1 0 0 1 1 1c0 1.25.2 2.45.57 3.57a1 1 0 0 1-.25 1z"/></svg>
      </li>
      <li>555 014 2269
        <svg viewBox="0 0 24 24"><rect x="6" y="1" width="12" height="22" rx="2"/></svg>
      </li>
      <li>555 014 2270
        <svg viewBox="0 0 24 24"><rect x="2" y="8" width="20" height="12" rx="1"/><rect x="6" y="2" width="12" height="6"/></svg>
      </li>
      <li>hello@veritynet.co
        <svg viewBox="0 0 24 24"><path d="M2 5h20v14H2z"/></svg>
      </li>
      <li>www.veritynet.co
        <svg viewBox="0 0 24 24"><circle cx="12" cy="12" r="10"/></svg>
      </li>
    </ul>
  </section>

</body>
</html>
```